We are Pacific Carriage Exchange from Japan to NewZealand

we are importing Japanese used cars from Japan to NewZealand and Motor vehicle parts trading in the world. we have company in Japan and New Zealand. we provide one stop service to import car from japan. we have two companies called PCX Ltd for car importing from japan and PCX Lubricants Ltd for car engine oil importing. also we are importing car parts under PCX Autohaus Ltd. we need logo and name card for our company. Company name is PCX LTD (Pacific Carriage Exchange) From japan we are sourcing newer European cars and 20-30 years old special sports limited model cars importing specialist. we are not normal car importer and retailer. also we are manufacture and supplying Motor vehicle Engine oil and parts from Korea and japan to New Zealand. Engine oil and part brand name is 'Ultra Z' we would like to introduce on business card. we want to show what we are doing as car importing, selling, parts and engine oil importing.

Target Market(s)

-Car buyer(customer)
-Mechanic shop
-Car dealers
-Car industry people
-Car & parts exporter/importer
-Engine oil reseller
-parts reseller

Industry/Entity Type

Car Dealer

Contact Information for Business Card

Dale Morrow
Director
17 Fennick Lane, Harlow Flats, Auckland 0589, New Zealand
+64215830142
pcx.limited@example-mail.nz
www.pcxwheels-example.co.nz
www.pcxexample.com

Colors
ffc214
9d9d9d
0255a3

Requirements
Must have
• * PCX Wheels Ltd(PCX LTD-car importing, sourcing and retailing)
• * PCX Lubricants Ltd(Engine Oil importing, sourcing and retailing)
• * PCX Autohaus Ltd(car parts and accessories importing, sourcing and retailing)
• * Ultra Z -Brand name of engine oil
• (We are wanting to make logo for PCX WHEELS and ULTRA Z MOTOR OIL)
Nice to have
• we would like to show us to our clients as professional, trustworthy, many experience. not well known in the market but unique indivisual company for clients.
Should not have
• we do not want to feel just 'car dealer' , 'importer' or normal sales

```html
<!DOCTYPE html>
<html lang="en">
<head>
<meta charset="utf-8">
<title>PCX Wheels Ltd – Business Card</title>
<link rel="stylesheet" href="https://fonts.googleapis.com/css2?family=Open+Sans:wght@400;600;700&display=swap">
<style>
  :root {
    --blue: #0255a3;
    --blue-deep: #013f7a;
    --yellow: #ffc214;
    --grey: #9d9d9d;
    --grey-light: #d4d4d4;
    --white: #ffffff;
    --stage: #ecebe8;
    --navy-text: #0b3d7a;
  }
  * { box-sizing: border-box; margin: 0; padding: 0; }
  html, body { width: 1200px; height: 913px; overflow: hidden; }
  body {
    background: var(--stage);
    font-family: "Open Sans", Arial, sans-serif;
    position: relative;
  }
  .card {
    position: absolute;
    width: 540px;
    height: 310px;
    border-radius: 16px;
    overflow: hidden;
    box-shadow: 0 6px 18px rgba(0,0,0,0.18);
  }
  /* Front */
  .card--front {
    left: 50px; top: 170px;
    background: linear-gradient(160deg, #1a6cb8 0%, var(--blue) 45%, var(--blue-deep) 100%);
    color: var(--white);
  }
  .card--front .edge-dot {
    position: absolute; left: -22px; top: 232px;
    width: 44px; height: 44px; border-radius: 50%;
    background: var(--yellow);
  }
  .card--front .brand {
    position: absolute; left: 40px; top: 58px;
  }
  .brand__name {
    font-weight: 700; font-size: 30px; letter-spacing: 1px;
    color: var(--grey-light); line-height: 1;
  }
  .brand__tagline {
    margin-top: 6px; font-size: 10px; color: var(--grey-light);
  }
  .card--front .divider {
    position: absolute; left: 40px; top: 120px;
    width: 460px; height: 1px; background: rgba(255,255,255,0.45);
  }
  .holder { position: absolute; left: 72px; top: 138px; }
  .holder__name {
    font-weight: 700; font-size: 21px; color: var(--yellow); letter-spacing: 0.5px;
  }
  .holder__role { font-size: 13px; letter-spacing: 1px; margin-top: 1px; }
  .holder__rule {
    width: 240px; height: 1px; background: rgba(255,255,255,0.45); margin: 8px 0 8px;
  }
  .address { font-size: 12.5px; color: var(--yellow); line-height: 1.45; }
  .contacts { list-style: none; margin-top: 6px; }
  .contacts li {
    display: flex; align-items: center; gap: 10px;
    font-size: 12.5px; color: var(--yellow); line-height: 1.6;
  }
  .contacts svg { width: 12px; height: 12px; flex: none; fill: var(--white); }

  /* Back */
  .card--back {
    left: 610px; top: 430px;
    background: var(--white);
    text-align: center;
  }
  .card--back .brand {
    position: absolute; left: 0; right: 0; top: 70px;
  }
  .card--back .brand__name {
    font-size: 40px; color: var(--grey); letter-spacing: 1.5px;
  }
  .offer {
    position: absolute; left: 0; right: 0; top: 150px;
    font-size: 11.5px; color: var(--navy-text); line-height: 1.5;
  }
  .offer strong { font-weight: 700; }
  .web {
    position: absolute; left: 0; right: 0; top: 254px;
    font-size: 13px; color: var(--navy-text); letter-spacing: 0.5px;
  }
</style>
</head>
<body>
  <section class="card card--front" aria-label="Business card front">
    <span class="edge-dot"></span>
    <div class="brand">
      <div class="brand__name">PCX WHEELS LTD</div>
      <div class="brand__tagline">Pacific Carriage Exchange Limited (PCX)</div>
    </div>
    <div class="divider"></div>
    <div class="holder">
      <div class="holder__name">DALE MORROW</div>
      <div class="holder__role">DIRECTOR</div>
      <div class="holder__rule"></div>
      <p class="address">17 Fennick Lane, Harlow Flats<br>Auckland 0589, New Zealand</p>
      <ul class="contacts">
        <li>
          <svg viewBox="0 0 24 24" aria-hidden="true"><path d="M6.6 10.8a15 15 0 0 0 6.6 6.6l2.2-2.2c.3-.3.7-.4 1-.2 1.1.4 2.3.6 3.6.6.6 0 1 .4 1 1V20c0 .6-.4 1-1 1A17 17 0 0 1 3 4c0-.6.4-1 1-1h3.5c.6 0 1 .4 1 1 0 1.3.2 2.5.6 3.6.1.3 0 .7-.2 1z"/></svg>
          +64215830142
        </li>
        <li>
          <svg viewBox="0 0 24 24" aria-hidden="true"><path d="M2 5h20v14H2zm2 2v.5l8 5 8-5V7zm16 10V9.8l-8 5-8-5V17z"/></svg>
          pcx.limited@example-mail.nz
        </li>
        <li>
          <svg viewBox="0 0 24 24" aria-hidden="true"><path d="M12 2a10 10 0 1 0 0 20 10 10 0 0 0 0-20zm7.9 9h-3.4a15 15 0 0 0-1.4-6A8 8 0 0 1 19.9 11zM12 4c1 1.3 2.3 3.8 2.5 7h-5C9.7 7.8 11 5.3 12 4zM8.9 5a15 15 0 0 0-1.4 6H4.1A8 8 0 0 1 8.9 5zM4.1 13h3.4a15 15 0 0 0 1.4 6A8 8 0 0 1 4.1 13zM12 20c-1-1.3-2.3-3.8-2.5-7h5c-.2 3.2-1.5 5.7-2.5 7zm3.1-1a15 15 0 0 0 1.4-6h3.4a8 8 0 0 1-4.8 6z"/></svg>
          www.pcxwheels-example.co.nz
        </li>
      </ul>
    </div>
  </section>

  <section class="card card--back" aria-label="Business card back">
    <div class="brand">
      <div class="brand__name">PCX WHEELS LTD</div>
    </div>
    <p class="offer">
      Ultra Z -Brand name of engine oil<br>
      <strong>PCX Wheels Ltd</strong>(PCX LTD-car importing, sourcing and retailing)<br>
      <strong>PCX Lubricants Ltd</strong>(Engine Oil importing, sourcing and retailing)<br>
      <strong>PCX Autohaus Ltd</strong>(car parts and accessories importing, sourcing and retailing)
    </p>
    <p class="web">www.pcxexample.com</p>
  </section>
</body>
</html>
```